Bright oak path business card

Bright oak path is a new online life insurance company providing instant quotes and policies to consumers.
Target Market(s)
Target market is both business to business as well as business to consumer
Can think out side of the box- We are an open minded bunch
Industry/Entity Type
Life Insurance
Requirements
Must have
- Our corporate Logo
Double sided
Website www.brightoakpath.com.au
Phone Number
Name & Position of each person etc.
Modern font

```html
<!DOCTYPE html>
<html lang="en">
<head>
<meta charset="utf-8">
<title>Bright oak path – business cards</title>
<link rel="stylesheet" href="https://fonts.googleapis.com/css2?family=Open+Sans:wght@400;600&display=swap">
<style>
  :root {
    --page-bg: #ffffff;
    --card-top: #ffffff;
    --card-bottom: #e4e4e4;
    --card-edge: #c9c9c9;
    --ink: #1f1f1f;
    --accent-orange: #ee7d22;
    --ring-blue: #3f8fc4;
    --ring-grey: #d6d6d6;
    --dot-peach: #f3c7a2;
    --dot-lime: #dde6b4;
    --text-font: "Open Sans", Arial, sans-serif;
  }
  * { box-sizing: border-box; margin: 0; padding: 0; }
  html, body { width: 1200px; height: 900px; overflow: hidden; background: var(--page-bg); }
  .canvas { position: relative; width: 1200px; height: 900px; font-family: var(--text-font); }

  .card {
    position: absolute;
    width: 668px;
    height: 430px;
    border-radius: 14px;
    border: 1px solid var(--card-edge);
    background: linear-gradient(180deg, var(--card-top) 0%, var(--card-top) 35%, var(--card-bottom) 100%);
    box-shadow: 0 3px 8px rgba(0,0,0,0.18);
    overflow: hidden;
  }
  .card--front { left: 48px; top: 10px; }
  .card--back  { left: 488px; top: 456px; }

  .brand-name {
    position: absolute;
    font-weight: 600;
    font-size: 52px;
    line-height: 1;
    letter-spacing: -1px;
    color: var(--ink);
  }
  .card--front .brand-name { left: 34px; top: 100px; }
  .card--back  .brand-name { left: 44px; top: 52px; }

  .decor { position: absolute; left: 0; top: 0; width: 668px; height: 430px; }

  .contact { position: absolute; left: 328px; color: var(--ink); }
  .card--front .contact { top: 262px; }
  .card--back  .contact { top: 268px; }
  .contact__name { font-size: 28px; font-weight: 400; color: var(--accent-orange); line-height: 34px; }
  .contact__role { font-size: 19px; line-height: 28px; margin-bottom: 8px; }
  .contact__line { font-size: 19px; line-height: 34px; }
  .contact__label { color: var(--accent-orange); margin-right: 4px; }
</style>
</head>
<body>
<main class="canvas">

  <section class="card card--front" aria-label="Business card, front">
    <svg class="decor" viewBox="0 0 668 430" aria-hidden="true">
      <circle cx="262" cy="330" r="46" fill="#f4f4f4" stroke="var(--ring-grey)" stroke-width="4"/>
      <circle cx="262" cy="330" r="38" fill="#ffffff" stroke="var(--ring-blue)" stroke-width="3"/>
    </svg>
    <p class="brand-name">Bright oak path</p>
    <div class="contact">
      <p class="contact__name">Mara Quinlan</p>
      <p class="contact__role">Director</p>
      <p class="contact__line"><span class="contact__label">P.</span>1300 555 019</p>
      <p class="contact__line"><span class="contact__label">W.</span>www.brightoakpath.com.au</p>
    </div>
  </section>

  <section class="card card--back" aria-label="Business card, back">
    <svg class="decor" viewBox="0 0 668 430" aria-hidden="true">
      <circle cx="418" cy="254" r="18" fill="var(--dot-peach)"/>
      <circle cx="510" cy="272" r="38" fill="var(--dot-lime)"/>
      <circle cx="558" cy="350" r="22" fill="var(--dot-peach)"/>
    </svg>
    <p class="brand-name">Bright oak path</p>
    <div class="contact">
      <p class="contact__name">Mara Quinlan</p>
      <p class="contact__role">Director</p>
      <p class="contact__line"><span class="contact__label">P.</span>1300 555 019</p>
      <p class="contact__line"><span class="contact__label">W.</span>www.brightoakpath.com.au</p>
    </div>
  </section>

</main>
</body>
</html>
```